Package design for supplement

We are looking to design a product packaing in Paperboard Jar. Our company sells varity of supplements. we had previously design in Stand up pouches but we needs new design in Jars. See attached all product information and logos

```html
<!DOCTYPE html>
<html lang="en">
<head>
<meta charset="utf-8">
<title>Olvera Naturals – Organic Psyllium Whole Husk Jar Label</title>
<link href="https://fonts.googleapis.com/css2?family=Marcellus&family=Lato:wght@400;700&display=swap" rel="stylesheet">
<style>
  :root {
    --backdrop: #a1a1a1;
    --paper: #f4f5ef;
    --sage: #dfe6cf;
    --sage-deep: #cfdcb8;
    --green: #0b8a3a;
    --green-dark: #00733a;
    --green-text: #138a3c;
    --slate: #3c4c56;
    --gold: #d9a936;
    --gold-light: #f6de8a;
    --white: #ffffff;
  }
  * { margin: 0; padding: 0; box-sizing: border-box; }
  html, body { width: 1200px; height: 1081px; overflow: hidden; }
  body { background: var(--backdrop); position: relative; }

  .jar-label {
    position: absolute;
    left: 423px; top: 262px;
    width: 354px; height: 600px;
    overflow: hidden;
    background:
      radial-gradient(ellipse 55% 45% at 55% 20%, var(--sage) 0%, transparent 70%),
      radial-gradient(ellipse 50% 60% at 45% 60%, var(--sage) 0%, transparent 75%),
      linear-gradient(100deg, var(--paper) 0%, var(--sage) 40%, var(--sage-deep) 60%, var(--paper) 100%);
  }

  .lid-title {
    position: absolute; left: 0; right: 0; top: 70px;
    text-align: center;
    font-family: "Marcellus", serif;
    font-size: 20px; line-height: 21px;
    color: var(--green-text);
  }

  .gold-band {
    position: absolute; left: 0; right: 0; height: 12px;
    background: linear-gradient(180deg, var(--gold) 0%, var(--gold-light) 45%, var(--gold) 100%);
  }
  .gold-band.top { top: 150px; }
  .gold-band.bottom { top: 568px; height: 14px; }

  .brand-name {
    position: absolute; left: 0; right: 0; top: 196px;
    text-align: center;
    font-family: "Marcellus", serif;
    font-size: 30px; line-height: 34px;
    color: var(--slate);
  }

  .product-seal {
    position: absolute; left: 0; top: 0; width: 354px; height: 600px;
  }

  .product-name {
    position: absolute; left: 84px; width: 200px; top: 292px;
    text-align: center;
    font-family: "Marcellus", serif;
    font-size: 27px; line-height: 28.5px;
    color: var(--green-text);
  }

  .plant-illustration {
    position: absolute; left: 233px; top: 322px; width: 122px; height: 172px;
    background: radial-gradient(ellipse at 50% 45%, rgba(90,170,90,0.35) 0%, rgba(90,170,90,0.12) 55%, transparent 75%);
  }

  .cert-badge {
    position: absolute; left: 22px; width: 32px; height: 32px;
    border-radius: 50%;
    background: var(--white);
    border: 2px solid var(--green-dark);
    box-shadow: 0 0 0 2px var(--white);
  }
  .cert-badge.organic { top: 457px; }
  .cert-badge.kosher { top: 508px; }

  .net-weight {
    position: absolute; left: 0; right: 0; top: 527px;
    text-align: center;
    font-family: "Lato", sans-serif;
    color: var(--white);
    font-size: 12.5px; line-height: 15px;
  }
  .net-weight strong { font-weight: 700; font-size: 13px; }
</style>
</head>
<body>
  <main class="jar-label">
    <p class="lid-title">ORGANIC PSYLLIUM<br>WHOLE HUSK</p>
    <div class="gold-band top"></div>

    <p class="brand-name">Olvera Naturals</p>

    <svg class="product-seal" viewBox="0 0 354 600" aria-hidden="true">
      <defs>
        <linearGradient id="goldRing" x1="0" y1="0" x2="1" y2="1">
          <stop offset="0" stop-color="#e9c25a"/>
          <stop offset="0.5" stop-color="#f5dc8c"/>
          <stop offset="1" stop-color="#d39a2a"/>
        </linearGradient>
      </defs>
      <path d="M0 404 C 60 420, 120 450, 178 477 C 240 445, 300 415, 354 398 L354 600 L0 600 Z" fill="var(--green)"/>
      <path d="M0 475 L178 478 L354 470 L354 600 L0 600 Z" fill="var(--green-dark)"/>
      <circle cx="183" cy="347" r="97" fill="none" stroke="url(#goldRing)" stroke-width="2.5"/>
    </svg>

    <div class="plant-illustration" role="img" aria-label="Line drawing of a flowering psyllium plant"></div>

    <p class="product-name">ORGANIC<br>PSYLLIUM<br>WHOLE<br>HUSK</p>

    <div class="cert-badge organic"></div>
    <div class="cert-badge kosher"></div>

    <p class="net-weight">Net Weight<br><strong>16oz (453.6g)</strong></p>

    <div class="gold-band bottom"></div>
  </main>
</body>
</html>
```